Modern Business Card

Modern professional business card with more than just logo and demographic info. Something memorable.

We are a trendy/modern chiropractic group with an emphasis on neurology, hence the minimalist-type brain logo. We want to convey that modern and technical aspect with professionalism and the elite nature of our practice environment.

```html
<!DOCTYPE html>
<html lang="en">
<head>
<meta charset="utf-8">
<title>Meridian Chiropractic – Business Card</title>
<link rel="stylesheet" href="https://fonts.googleapis.com/css2?family=Open+Sans:wght@400&family=Tinos:wght@400&display=swap">
<style>
  :root {
    --backdrop: #4f5358;
    --card: #ffffff;
    --brand-blue: #437cc0;
    --ink: #2a2a2a;
    --ink-soft: #3a3a3a;
  }
  * { box-sizing: border-box; margin: 0; padding: 0; }
  html, body { width: 1200px; height: 1200px; overflow: hidden; }
  body {
    background: var(--backdrop);
    font-family: "Open Sans", Arial, sans-serif;
    color: var(--ink);
  }
  .canvas {
    width: 1200px; height: 1200px;
    display: flex; flex-direction: column;
    align-items: center; justify-content: center;
    gap: 60px;
  }
  .card {
    position: relative;
    width: 840px; height: 480px;
    background: var(--card);
    overflow: hidden;
  }

  /* Back side */
  .card-back {
    display: flex; flex-direction: column;
    align-items: center; justify-content: center;
    gap: 26px;
  }
  .back-mark {
    width: 150px; height: 150px;
    border-radius: 50%;
    background: var(--brand-blue);
  }
  .back-name {
    font-family: "Tinos", "Times New Roman", serif;
    font-size: 34px; letter-spacing: 2px;
    color: var(--brand-blue);
    text-transform: uppercase;
  }

  /* Front side */
  .holder { position: absolute; left: 62px; top: 44px; }
  .holder-name {
    font-family: "Tinos", "Times New Roman", serif;
    font-size: 44px; line-height: 1;
    color: var(--brand-blue);
    text-transform: uppercase;
  }
  .holder-title { font-size: 20px; margin-top: 8px; color: var(--ink); }

  .contacts {
    position: absolute; left: 68px; top: 178px;
    display: flex; flex-direction: column; gap: 30px;
  }
  .contact-row { display: flex; align-items: center; gap: 14px; }
  .contact-icon { width: 32px; height: 32px; flex: none; }
  .contact-lines { font-size: 24px; line-height: 1.45; color: var(--ink-soft); }
  .accent { color: var(--brand-blue); }

  .company {
    position: absolute; right: 60px; top: 178px;
    display: flex; align-items: center; gap: 18px;
  }
  .company-mark {
    width: 92px; height: 92px; border-radius: 50%;
    background: var(--brand-blue);
  }
  .company-name {
    font-family: "Tinos", "Times New Roman", serif;
    font-size: 44px; line-height: 1.0;
    color: var(--ink);
    text-transform: uppercase;
  }
  .company-name span { display: block; }
  .company-name .sub { font-size: 36px; letter-spacing: 1px; }

  .base-band {
    position: absolute; left: 0; right: 0; bottom: 0;
    height: 36px; background: var(--brand-blue);
  }
</style>
</head>
<body>
<main class="canvas">
  <section class="card card-back" aria-label="Card back">
    <div class="back-mark"></div>
    <div class="back-name">Meridian Chiropractic</div>
  </section>

  <section class="card card-front" aria-label="Card front">
    <header class="holder">
      <h1 class="holder-name">Adam Carter</h1>
      <p class="holder-title">Neurologist</p>
    </header>

    <div class="contacts">
      <div class="contact-row">
        <svg class="contact-icon" viewBox="0 0 32 32" aria-hidden="true">
          <circle cx="16" cy="16" r="16" fill="var(--brand-blue)"/>
          <path d="M16 7c-3.6 0-6.3 2.7-6.3 6.2 0 4.4 6.3 11.3 6.3 11.3s6.3-6.9 6.3-11.3C22.3 9.7 19.6 7 16 7z" fill="#fff"/>
          <circle cx="16" cy="13.2" r="2.4" fill="var(--brand-blue)"/>
        </svg>
        <div class="contact-lines">Dummy city<br>Dummy Country Land</div>
      </div>
      <div class="contact-row">
        <svg class="contact-icon" viewBox="0 0 32 32" aria-hidden="true">
          <circle cx="16" cy="16" r="16" fill="var(--brand-blue)"/>
          <path d="M7 13c0-2.5 4-4 9-4s9 1.5 9 4v1.5h-4.2V12.6c-1.4-.5-3-.7-4.8-.7s-3.4.2-4.8.7v1.9H7z" fill="#fff"/>
          <path d="M10 16.5l2.5-3h7l2.5 3V23H10z" fill="#fff"/>
          <circle cx="16" cy="19" r="2" fill="var(--brand-blue)"/>
        </svg>
        <div class="contact-lines">1-234-567890<br>1-234-567890</div>
      </div>
      <div class="contact-row">
        <svg class="contact-icon" viewBox="0 0 32 32" aria-hidden="true">
          <circle cx="16" cy="16" r="16" fill="var(--brand-blue)"/>
          <circle cx="16" cy="16" r="9" fill="none" stroke="#fff" stroke-width="2"/>
          <ellipse cx="16" cy="16" rx="4" ry="9" fill="none" stroke="#fff" stroke-width="1.6"/>
          <line x1="7" y1="16" x2="25" y2="16" stroke="#fff" stroke-width="1.6"/>
        </svg>
        <div class="contact-lines">adam@<span class="accent">meridianchiro</span>.com<br>www.<span class="accent">meridianchiro</span>.com</div>
      </div>
    </div>

    <div class="company">
      <div class="company-mark"></div>
      <div class="company-name"><span>Meridian</span><span class="sub">Chiropractic</span></div>
    </div>

    <div class="base-band"></div>
  </section>
</main>
</body>
</html>
```